" A VELAR possui basicamente DUAS atividades (ou podemos chamar de serviços). A primeira diz respeito a ESTRUTURAÇAO DE NOVOS NEGOCIOS ou DESENVOLVIMENTO DE NOVOS NEGOCIOS, conhecido pelo termo em inglês de BUSINESS DEVELOPMENT. Neste caso a VELAR identifica produtos e tecnologias consagradas em outros mercados e estrutura um novo negócio no Brasil com o objetivo de aplicar esta tecnologia/produto no mercado Brasileiro. Para tanto, aplica uma metodologia própria de estruturaçao de negócios. A segunda atividade é puramente de CONSULTORIA, dando assessoria em processos de FUSAO&AQUISIÇAO, conhecido pelo mercado como processos de M&A (Merge & Acquisition). Neste caso a VELAR oferece toda a sua experiência para assessorar principal o VENDEDOR, isto é, a empresa que está sendo comprada. "

```html
<!DOCTYPE html>
<html lang="pt-BR">
<head>
<meta charset="utf-8">
<title>VELAR – Business Development</title>
<link rel="stylesheet" href="https://fonts.googleapis.com/css2?family=Source+Sans+3:ital,wght@0,400;0,600;0,700;1,400&display=swap">
<style>
:root{
  --navy:#12335a;
  --navy-dark:#0c2541;
  --orange:#f05a22;
  --white:#ffffff;
  --text:#3a3f47;
  --photo-a:#b9c3cc;
  --photo-b:#e6e9ec;
  --quote-band:rgba(30,30,34,.72);
}
*{box-sizing:border-box;margin:0;padding:0}
html,body{width:1200px;height:1200px;overflow:hidden;background:var(--white);font-family:"Source Sans 3",sans-serif}
.page{position:relative;width:1200px;height:1200px}

.brand{position:absolute;left:132px;top:16px;height:64px;display:flex;align-items:center;gap:14px}
.brand-dot{width:58px;height:58px;border-radius:50%;background:var(--orange);flex:none}
.brand-name{font-size:64px;font-weight:700;color:var(--navy);letter-spacing:3px;line-height:1}

.main-nav{position:absolute;left:620px;top:0;width:508px;height:44px;background:var(--navy);display:flex}
.main-nav a{color:var(--white);text-decoration:none;font-weight:700;font-size:22px;line-height:44px;padding:0 22px;letter-spacing:.5px}
.main-nav .is-active{color:var(--orange)}
.main-nav .nav-contact{margin-left:auto}

.submenu{position:absolute;left:800px;top:44px;width:180px;background:var(--navy-dark);z-index:3}
.submenu a{display:block;color:var(--white);font-weight:700;font-size:18px;line-height:22px;padding:10px 20px;text-decoration:none;border-bottom:2px solid var(--white)}
.submenu a:last-child{border-bottom:0}

.social-bar{position:absolute;left:980px;top:44px;width:148px;height:52px;background:var(--orange);display:flex;align-items:center;justify-content:center;gap:16px}
.social-bar svg{display:block}

.hero{position:absolute;left:72px;top:96px;width:1056px;height:552px;background:linear-gradient(135deg,var(--photo-b),var(--photo-a) 60%,#8c99a6)}
.hero-quote{position:absolute;left:0;right:0;top:324px;height:156px;background:var(--quote-band);color:var(--white);text-align:right;padding:26px 16px 0 0}
.hero-quote p{font-size:30px;line-height:38px}
.hero-quote cite{display:block;font-style:normal;font-weight:700;font-size:32px;margin-top:6px;letter-spacing:.5px}

.slider-bar{position:absolute;left:72px;top:648px;width:1056px;height:36px;background:var(--orange);display:flex;justify-content:center;align-items:center;gap:12px}
.slider-bar span{width:16px;height:16px;border:2px solid var(--white);border-radius:50%}
.slider-bar span.on{background:var(--white)}

.section-title{position:absolute;left:100px;top:710px;font-size:72px;font-weight:600;color:var(--navy);letter-spacing:-1px;line-height:1.1}
.portrait{position:absolute;left:178px;top:806px;width:266px;height:318px;background:linear-gradient(180deg,#cfd3d7,#8a9097)}
.content{position:absolute;left:466px;top:810px;width:650px;font-style:italic;font-size:19px;line-height:23px;color:var(--text)}
.content p{margin-bottom:18px}
.content .quote{padding-left:32px}
</style>
</head>
<body>
<div class="page">
  <div class="brand"><span class="brand-dot"></span><span class="brand-name">VELAR</span></div>

  <nav class="main-nav">
    <a href="#">A EMPRESA</a>
    <a href="#" class="is-active">SERVIÇOS &#9662;</a>
    <a href="#" class="nav-contact">CONTATO</a>
  </nav>
  <div class="submenu">
    <a href="#">BUSINESS DEVELOPMENT</a>
    <a href="#">M &amp; A CONSULTING</a>
  </div>
  <div class="social-bar">
    <svg width="26" height="24" viewBox="0 0 26 24" aria-label="comentar"><path d="M2 2 H24 V16 H11 L5 22 V16 H2 Z" fill="#fff"/></svg>
    <svg width="26" height="24" viewBox="0 0 26 24" aria-label="compartilhar"><g fill="#fff"><circle cx="20" cy="5" r="4"/><circle cx="6" cy="12" r="4"/><circle cx="20" cy="19" r="4"/></g><path d="M20 5 L6 12 L20 19" fill="none" stroke="#fff" stroke-width="2.5"/></svg>
    <svg width="30" height="22" viewBox="0 0 30 22" aria-label="e-mail"><rect x="1" y="1" width="28" height="20" fill="#fff"/><path d="M1 1 L15 12 L29 1" fill="none" stroke="#f05a22" stroke-width="2"/></svg>
  </div>

  <div class="hero" role="img" aria-label="Foto de equipe de negócios reunida em volta de uma mesa com laptop">
    <blockquote class="hero-quote">
      <p>“O destino não é uma questão de sorte, é uma questão de escolha.<br>Não é algo que se deve esperar, é algo que se deve alcançar.”</p>
      <cite>HENRIQUE ALVES DUARTE</cite>
    </blockquote>
  </div>
  <div class="slider-bar"><span></span><span></span><span class="on"></span></div>

  <h1 class="section-title">Business Development</h1>
  <div class="portrait" role="img" aria-label="Retrato de consultor executivo de terno"></div>
  <div class="content">
    <p>Nossa vocação está em identificar tecnologias em outros mercados, principalmente na Ásia, Estados Unidos, Europa e Israel, e trazê-las para o mercado Brasileiro.</p>
    <p>Não fazemos o que o mercado chama de “Start Up”.<br>Segundo a Associação Nacional de Empresas Emergentes, Startup é:</p>
    <p class="quote">“Uma empresa de base tecnológica, com um modelo de negócios repetível e escalável, que possui elementos de inovação e trabalha em condições de extrema incerteza.”, grifou-se.</p>
    <p>Normalmente uma Startup está relacionada com uma tecnologia completamente nova e desconhecida. Neste caso as condições de incerteza de sucesso são extremas.</p>
  </div>
</div>
</body>
</html>
```